DOVVRANTI Label and bottle design

We have already provided attached an idea concept of a label and bottle shape example, we now require designers to take this basic concept and advance it to the final label design using your own design creativity.
Please see attached the full product brief

```html
<!DOCTYPE html>
<html lang="en">
<head>
<meta charset="utf-8">
<title>DOVVRANTI INKSOLVE Label</title>
<link rel="stylesheet" href="https://fonts.googleapis.com/css2?family=Montserrat:wght@400;500;600;700;800&display=swap">
<style>
:root{
  --ink-black:#141414;
  --brand-yellow:#f3e817;
  --paper:#ffffff;
  --hazard-red:#e32222;
  --text-dark:#1b1b1b;
}
*{margin:0;padding:0;box-sizing:border-box}
html,body{width:922px;height:1200px;overflow:hidden;background:var(--paper)}
body{font-family:"Montserrat",sans-serif;position:relative}
.label{position:absolute;left:21px;top:253px;width:1312px;height:1034px;transform:scale(0.6707);transform-origin:0 0;background:var(--brand-yellow);overflow:hidden}
.label-shapes{position:absolute;left:0;top:0}
.abs{position:absolute}
.brand-name{left:0;width:660px;top:140px;text-align:center;font-weight:800;font-size:84px;letter-spacing:2px;color:var(--brand-yellow)}
.tagline{left:0;width:660px;top:288px;text-align:center;color:var(--paper);font-weight:500;font-size:14.5px;letter-spacing:.3px}
.suitable-title{left:61px;top:366px;color:var(--paper);font-weight:500;font-size:20px;letter-spacing:.5px}
.ink-type{top:490px;width:108px;text-align:center;color:var(--paper);font-size:10.5px;font-weight:500;line-height:12px}
.product-line{left:58px;font-weight:700;font-size:113px;line-height:1;letter-spacing:-1px}
.product-line.first{top:585px;color:var(--brand-yellow)}
.product-line.second{top:695px;color:var(--paper)}
.product-type{left:65px;top:826px;width:400px;height:31px;background:var(--brand-yellow);color:var(--ink-black);font-weight:600;font-size:21px;line-height:31px;text-align:center}
.claims{left:66px;top:882px;color:var(--paper);font-weight:500;font-size:18.5px;line-height:28px;letter-spacing:.2px}
.net-weight{left:520px;top:540px;width:104px;text-align:center;color:var(--ink-black);font-weight:600;font-size:40px;line-height:44px}
.info{color:var(--text-dark);font-size:13px;line-height:21.2px;font-weight:500;letter-spacing:-.15px}
.section-head{display:flex;align-items:center;gap:8px;font-weight:700;font-size:13.5px}
.section-head::after{content:"";flex:1;height:1.5px;background:var(--text-dark)}
.uses{left:696px;top:34px;width:568px}
.directions{left:696px;top:210px;width:568px;height:274px;border:1.5px solid var(--text-dark);border-radius:18px}
.directions-title{position:absolute;left:0;right:0;top:-12px;text-align:center;line-height:22px}
.directions-title span{background:var(--brand-yellow);padding:0 36px;font-weight:700;font-size:13.5px}
.step{position:absolute;width:258px}
.step b{display:block;font-weight:700}
.extra{left:696px;top:498px;width:280px}
.caution{left:1002px;top:498px;width:268px}
.caution b{font-weight:700}
.safety{left:697px;top:604px;width:567px;height:264px;background:var(--paper);border-radius:18px}
.safety-icon{position:absolute;left:14px;top:64px}
.safety-text{position:absolute;left:165px;top:20px;width:390px;font-size:12px;line-height:21px}
.safety-text .section-head{width:220px;margin-bottom:16px}
.safety-foot{margin-top:20px;font-weight:700}
.company{left:697px;top:893px;width:567px;height:100px;background:var(--ink-black);border-radius:14px}
.company-name{position:absolute;left:26px;top:36px;color:var(--brand-yellow);font-weight:800;font-size:22px;letter-spacing:1px}
.company-details{position:absolute;left:200px;top:16px;color:var(--paper);font-size:12px;line-height:21px;font-weight:500}
</style>
</head>
<body>
<div class="label">
  <svg class="label-shapes" width="1312" height="1034" viewBox="0 0 1312 1034" aria-hidden="true">
    <polygon points="0,0 657,0 657,316 626,316 434,608 626,879 657,879 657,1034 0,1034" fill="var(--ink-black)"/>
    <g stroke="var(--brand-yellow)" stroke-width="3" fill="none">
      <line x1="406" y1="0" x2="461" y2="84"/>
      <polyline points="471,316 400,416 0,416"/>
      <polyline points="400,416 330,533 0,533"/>
      <line x1="142" y1="416" x2="142" y2="533"/>
      <line x1="250" y1="416" x2="250" y2="533"/>
    </g>
    <g stroke="var(--brand-yellow)" stroke-width="2" fill="none" stroke-linecap="round">
      <circle cx="87" cy="450" r="9"/>
      <path d="M83 459v6h8v-6M87 433v-5M72 450h-5M107 450h-5M76 439l-3-3M98 439l3-3"/>
      <path d="M95 462c3 5 4 7 4 9a4 4 0 0 1-8 0c0-2 1-4 4-9z"/>
      <rect x="181" y="438" width="24" height="28" rx="2"/>
      <ellipse cx="193" cy="438" rx="12" ry="3"/>
      <path d="M193 446l6 11h-12z"/>
      <path d="M210 455c3 5 4 7 4 9a4 4 0 0 1-8 0c0-2 1-4 4-9z"/>
      <path d="M292 433v10l-8 18h22l-8-18v-10M289 433h12"/>
      <circle cx="292" cy="455" r="1.5"/><circle cx="298" cy="457" r="1.5"/>
      <path d="M313 453c3 5 4 7 4 9a4 4 0 0 1-8 0c0-2 1-4 4-9z"/>
    </g>
  </svg>

  <div class="abs brand-name">DOVVRANTI</div>
  <div class="abs tagline">PROFESSIONAL CLEANING | MAXIMUM PERFORMANCE</div>
  <div class="abs suitable-title">SUITABLE FOR</div>
  <div class="abs ink-type" style="left:33px">UV BASED<br>INK</div>
  <div class="abs ink-type" style="left:142px">SOLVENT<br>BASED INK</div>
  <div class="abs ink-type" style="left:246px">WATER<br>BASED INKS</div>

  <div class="abs product-line first">INK</div>
  <div class="abs product-line second">SOLVE</div>
  <div class="abs product-type">ADVANCED ANILOXCLEANING GEL</div>
  <div class="abs claims">NON CAUSTIC | NON TOXIC |<br>NON FLAMMABLE | NON CORROSIVE</div>
  <div class="abs net-weight">1<br>KG</div>

  <div class="abs info uses">
    <div class="section-head">Uses</div>
    <p>INKSOLVE is a highly concentrated, powerful cleaning gel formulated to safely remove solvent-based, water-based, and UV inks from anilox rollers. It's thickened formula clings to surfaces, allowing deep penetration into anilox cells and is safe for use on both ceramic and chrome rollers. INKSOLVE Gel is also suitable for general pressroom cleaning of machinery, components and floors. Additionally, it can be used to remove most varnishes, coatings, and emulsion adhesives.</p>
  </div>

  <div class="abs info directions">
    <div class="directions-title"><span>Directions</span></div>
    <div class="step" style="left:8px;top:16px"><b>1. Apply</b>Apply INKSOLVE Gel directly to the surface of the anilox roller using an anilox cleaning pad or brush. Ensure full and even coverage with a thick layer of gel.</div>
    <div class="step" style="left:8px;top:178px"><b>3. Agitate</b>Use a anilox cleaning pad or brush to agitate and remove stubborn ink deposits.</div>
    <div class="step" style="left:298px;top:16px"><b>2. Dwell Time</b>Allow the gel to sit for 10–15 minutes</div>
    <div class="step" style="left:298px;top:80px"><b>4. RINSE THOROUGHLY</b>Rinse the roller thoroughly with warm water to remove all residue.</div>
    <div class="step" style="left:298px;top:178px"><b>5. Dry</b>Wipe dry with a clean lint-free cloth making sure the roller is completely dry before returning to production.</div>
  </div>

  <div class="abs info extra">INKSOLVE Gel can also be used for general press cleaning (rubber rollers , ink trays, doctor blades, press room floors etc)</div>
  <div class="abs info caution"><b>Caution-</b> pre testing on all surfaces is recommended before use.<br><span style="display:block;height:8px"></span><b>For more information</b><br>see full product data sheet.</div>

  <div class="abs info safety">
    <svg class="safety-icon" width="134" height="134" viewBox="0 0 134 134" aria-hidden="true">
      <rect x="24" y="24" width="86" height="86" transform="rotate(45 67 67)" fill="var(--paper)" stroke="var(--hazard-red)" stroke-width="6"/>
      <path d="M61 38h12l-3 40h-6z" fill="var(--hazard-red)"/>
      <circle cx="67" cy="90" r="6" fill="var(--hazard-red)"/>
    </svg>
    <div class="safety-text">
      <div class="section-head">Health and Safety</div>
      <p><b>Contains</b> - &lt;5% Non-Ionic surfactants<br>WARNING Contains: Alcohols, C9-11, ethoxylated.<br>Causes skin irritation. Causes serious eye irritation. Wash hands thoroughly after handling. Wear eye protection.<br>IF IN EYES: Rinse cautiously with water for several minutes. Remove contact lenses, if present and easy to do. Continue rinsing. If eye irritation persists: Get medical advice/attention.</p>
      <p class="safety-foot">See SDS for full safety information</p>
    </div>
  </div>

  <div class="abs company">
    <div class="company-name">DOVVRANTI</div>
    <div class="company-details">DOVVRANTI LTD<br>48 Harbour Lane, Dundee, DD1 3QX<br>E - info@dovvranti.co.uk | W - www.dovvranti.co.uk</div>
  </div>
</div>
</body>
</html>
```